Zielgruppe
Online-/Offline Marktplatz - Es ist ein Online Marktplatz, jedoch auch mit diversen Möglichkeiten für Dienstleister und Gastronomie. Wir sind nicht nur Online sondern haben auch Stores direkt in den Zentren der jeweiligen Städte und verbinden so online und Offline Shopping.
Aufgabenstellung
Ausdruckstarke Übersicht aller Möglichkeiten und Vorteile für den Händler - Klares Design
Die Broschüre erhält ein DIN A 4 Format über 8 Seiten.
Cover ( Foto von der Stadt Lübeck - ist im Anhang )
Hinteres Cover ( Foto lächelnde Frau einbauen ist im Anhang )
1 Seite Produktübersicht
3 Seiten detailierte Übersicht
1 Seite zusätzliche Vorteile
Vorstellungen vom Cover und backcover habe ich gerade hochgeladen - es sollte ein nicht zu dunkel aber dunkles Blau sein - schlichtes Design
und die fehlende Seite entwerfe ich gerade.
Farben und Inspirationen können Sie von der Webseite
www.sonnenhofmarktnord.de entnehmen.
Texte und Fotos liefern wir, wenn das Grunddesign der Broschüre steht.

```html
<!DOCTYPE html>
<html lang="de">
<head>
<meta charset="utf-8">
<title>Broschüre – Händlerübersicht</title>
<link rel="stylesheet" href="https://fonts.googleapis.com/css2?family=Montserrat:wght@700;800&family=Open+Sans:wght@400;600;700&display=swap">
<style>
  :root{
    --bg:#ececec;
    --paper:#ffffff;
    --red:#e8232a;
    --red-deep:#c8141b;
    --blue:#1f5fb8;
    --navy:#0f3d91;
    --ink:#333333;
    --muted:#8a8a8a;
    --rule:#d4d4d4;
  }
  *{box-sizing:border-box;margin:0;padding:0}
  html,body{width:1200px;height:2400px;overflow:hidden;background:var(--bg)}
  body{position:relative;font-family:"Open Sans",Arial,sans-serif;color:var(--ink)}

  .spread{position:absolute;left:110px;width:980px;height:693px;display:flex;box-shadow:0 18px 40px rgba(0,0,0,.18)}
  .spread--covers{top:60px}
  .spread--services{top:833px}
  .spread--advantages{top:1606px}
  .page{position:relative;width:490px;height:693px;background:var(--paper);overflow:hidden}
  .page + .page{box-shadow:inset 14px 0 18px -14px rgba(0,0,0,.25)}

  /* brand name */
  .brand{display:flex;align-items:center;gap:6px;font-family:"Open Sans",Arial,sans-serif;font-weight:700;font-size:13px;color:var(--ink)}
  .brand-dot{width:12px;height:12px;border-radius:50%;background:var(--red)}
  .page-brand{position:absolute;top:26px;right:30px}

  /* back cover */
  .back-art{position:absolute;inset:0}
  .back-contact{position:absolute;left:150px;top:500px;color:#fff}
  .back-contact .brand{color:#fff;font-size:16px;margin-bottom:22px}
  .back-contact .brand-dot{background:#fff}
  .back-contact p{font-size:13px;line-height:1.55}
  .back-contact p + p{margin-top:14px}

  /* front cover */
  .cover-heart{position:absolute;left:55px;top:95px;width:380px;height:400px}
  .cover-title{position:absolute;right:40px;bottom:70px;text-align:right;font-family:"Montserrat",Arial,sans-serif;font-weight:800;font-size:34px;line-height:1.08;color:#3a3a3a}
  .cover-title .accent{color:var(--blue)}

  /* inner page chrome */
  .page-foot{position:absolute;left:0;right:0;bottom:0;height:34px}
  .page-foot .band{position:absolute;left:0;right:0;top:0;height:6px;background:linear-gradient(90deg,var(--navy),var(--blue))}
  .page-foot span{position:absolute;top:14px;font-size:8px;color:var(--blue)}
  .page-foot .title{left:30px}
  .page-foot .num{right:30px}

  .page-heading{position:absolute;left:34px;top:88px;font-family:"Montserrat",Arial,sans-serif;font-weight:800;font-size:20px;color:#2b2b2b;letter-spacing:.3px}
  .page-heading .accent{color:var(--blue)}

  /* services grid */
  .service-grid{position:absolute;left:34px;top:135px;right:34px;display:grid;grid-template-columns:repeat(3,1fr);gap:12px}
  .service-tile{position:relative;height:110px;border-radius:12px;overflow:hidden}
  .service-tile span{position:absolute;left:10px;bottom:10px;font-family:"Montserrat",Arial,sans-serif;font-weight:700;font-size:10px;line-height:1.2;color:#fff}

  /* service rows */
  .service-list{position:absolute;left:30px;right:30px;top:80px}
  .service{display:grid;grid-template-columns:150px 1fr;column-gap:16px;height:190px}
  .service-photo{height:96px;border-radius:10px}
  .need{grid-column:1;grid-row:2;display:flex;align-items:center;justify-content:flex-end;gap:5px;font-size:7.5px;font-weight:700;margin-top:6px}
  .box{width:9px;height:9px;border:1.2px solid var(--blue);border-radius:2px}
  .service-body{grid-column:2;grid-row:1 / span 2}
  .service-body h3{font-family:"Montserrat",Arial,sans-serif;font-weight:700;font-size:11.5px;color:#2b2b2b;margin-bottom:5px}
  .service-body h3 span{color:var(--blue)}
  .service-body p{font-size:7.5px;line-height:1.5;color:#555}
  .notes{margin-top:8px}
  .notes .label{display:block;font-size:7.5px;font-weight:700;margin-bottom:2px}
  .notes i{display:block;height:14px;border-bottom:1px solid var(--rule)}

  /* advantages */
  .adv-heading{position:absolute;left:34px;top:92px;font-family:"Montserrat",Arial,sans-serif;font-weight:800;font-size:15px;color:#2b2b2b}
  .adv-heading .accent{color:var(--blue)}
  .adv-list{position:absolute;left:34px;right:34px;top:140px;list-style:none}
  .adv-list li{display:flex;gap:14px;align-items:flex-start;margin-bottom:18px}
  .adv-list svg{flex:none;width:16px;height:16px;margin-top:2px}
  .adv-list p{font-size:8.5px;line-height:1.55;color:#555}
</style>
</head>
<body>

<!-- Covers -->
<section class="spread spread--covers">
  <article class="page page--back">
    <svg class="back-art" viewBox="0 0 490 693" preserveAspectRatio="none">
      <defs>
        <linearGradient id="streetTone" x1="0" y1="0" x2="1" y2="1">
          <stop offset="0" stop-color="#b9b3ad"/>
          <stop offset=".5" stop-color="#8c7f78"/>
          <stop offset="1" stop-color="#c9c2bb"/>
        </linearGradient>
        <linearGradient id="redPanel" x1="0" y1="0" x2="1" y2="1">
          <stop offset="0" stop-color="#f2333a"/>
          <stop offset="1" stop-color="#d3161d"/>
        </linearGradient>
      </defs>
      <rect width="490" height="420" fill="url(#streetTone)" role="img" aria-label="Foto: lächelnde Frau in einer Einkaufsstraße"/>
      <path d="M0 330 C120 330 250 320 300 250 C350 180 380 70 490 40 L490 693 L0 693Z" fill="url(#redPanel)"/>
    </svg>
    <div class="back-contact">
      <div class="brand"><b class="brand-dot"></b>sonnenhofmarktnord</div>
      <p>Lindenweg 7, 23554<br>Lübeck, Deutschland</p>
      <p>info@sonnenhofmarktnord.de<br>www.sonnenhofmarktnord.de</p>
    </div>
  </article>

  <article class="page page--front">
    <div class="brand page-brand"><b class="brand-dot"></b>sonnenhofmarktnord</div>
    <svg class="cover-heart" viewBox="0 0 100 100" role="img" aria-label="Luftbild der Lübecker Altstadt mit Holstentor">
      <defs>
        <linearGradient id="cityTone" x1="0" y1="0" x2="1" y2="1">
          <stop offset="0" stop-color="#6f9aa6"/>
          <stop offset=".45" stop-color="#c8734a"/>
          <stop offset="1" stop-color="#8c4a30"/>
        </linearGradient>
      </defs>
      <path d="M50 94 C22 74 2 54 2 30 C2 14 14 4 28 4 C39 4 46 11 50 21 C54 11 61 4 72 4 C86 4 98 14 98 30 C98 54 78 74 50 94Z" fill="url(#cityTone)" stroke="#e8232a" stroke-width="4" stroke-linejoin="round"/>
    </svg>
    <h1 class="cover-title">WAS<br><span class="accent">SIND</span><br>WIR</h1>
  </article>
</section>

<!-- Services overview + details -->
<section class="spread spread--services">
  <article class="page">
    <div class="brand page-brand"><b class="brand-dot"></b>sonnenhofmarktnord</div>
    <h2 class="page-heading">UNSERE <span class="accent">LEISTUNGEN</span></h2>
    <div class="service-grid">
      <div class="service-tile" role="img" aria-label="Foto: Händler im Laden" style="background:linear-gradient(160deg,#c79a6d,#e8232a)"><span>Your Service<br>One Goes Here</span></div>
      <div class="service-tile" role="img" aria-label="Foto: Arbeitsplatz mit Laptops" style="background:linear-gradient(160deg,#4a4a4a,#e8232a)"><span>Your Service<br>Two Goes Here</span></div>
      <div class="service-tile" role="img" aria-label="Foto: helle Ladenpassage" style="background:linear-gradient(160deg,#d7e3ea,#e8232a)"><span>Your Service<br>Three Goes Here</span></div>
      <div class="service-tile" role="img" aria-label="Foto: Wohnhaus" style="background:linear-gradient(160deg,#9fb8cf,#e8232a)"><span>Your Service<br>Four Goes Here</span></div>
      <div class="service-tile" role="img" aria-label="Foto: Altstadt am Wasser" style="background:linear-gradient(160deg,#3d78b8,#e8232a)"><span>Your Service<br>Five Goes Here</span></div>
      <div class="service-tile" role="img" aria-label="Foto: gedeckter Tisch mit Speisen" style="background:linear-gradient(160deg,#d99a3a,#e8232a)"><span>Your Service<br>Six Goes Here</span></div>
      <div class="service-tile" role="img" aria-label="Foto: Konzertpublikum" style="background:linear-gradient(160deg,#8a5a2a,#e8232a)"><span>Your Service<br>Seven Goes Here</span></div>
      <div class="service-tile" role="img" aria-label="Foto: Straße mit Backsteinhäusern" style="background:linear-gradient(160deg,#b07a6a,#e8232a)"><span>Your Service<br>Eight Goes Here</span></div>
      <div class="service-tile" role="img" aria-label="Foto: grüner Park" style="background:linear-gradient(160deg,#4f7a3a,#e8232a)"><span>Your Service<br>Nine Goes Here</span></div>
      <div class="service-tile" role="img" aria-label="Foto: Bahnhofshalle" style="background:linear-gradient(160deg,#9aa0a6,#e8232a)"><span>Your Service<br>Ten Goes Here</span></div>
      <div class="service-tile" role="img" aria-label="Foto: Gruppe im Café" style="background:linear-gradient(160deg,#a6765a,#e8232a)"><span>Your Service<br>Eleven Goes Here</span></div>
      <div class="service-tile" role="img" aria-label="Foto: moderne Glasfassade" style="background:linear-gradient(160deg,#7cae86,#e8232a)"><span>Your Service<br>Twelve Goes Here</span></div>
    </div>
    <footer class="page-foot"><i class="band"></i><span class="title">Brochure Title Goes Here</span><span class="num">Seite 2</span></footer>
  </article>

  <article class="page">
    <div class="brand page-brand"><b class="brand-dot"></b>sonnenhofmarktnord</div>
    <div class="service-list">
      <div class="service">
        <div class="service-photo" role="img" aria-label="Foto: Händler im Laden" style="background:linear-gradient(135deg,#c79a6d,#7a4a2a)"></div>
        <div class="need">Brauche ich: <b class="box"></b></div>
        <div class="service-body">
          <h3>Your Service One <span>Goes Here</span></h3>
          <p>Kurze Beschreibung der Leistung mit den wichtigsten Vorteilen für Händler vor Ort und online, klar und verständlich formuliert.</p>
          <div class="notes"><span class="label">Notizen/Fragen:</span><i></i><i></i><i></i></div>
        </div>
      </div>
      <div class="service">
        <div class="service-photo" role="img" aria-label="Foto: Arbeitsplatz mit Laptops" style="background:linear-gradient(135deg,#6a6a6a,#2e2e2e)"></div>
        <div class="need">Brauche ich: <b class="box"></b></div>
        <div class="service-body">
          <h3>Your Service One <span>Goes Here</span></h3>
          <p>Kurze Beschreibung der Leistung mit den wichtigsten Vorteilen für Händler vor Ort und online, klar und verständlich formuliert.</p>
          <div class="notes"><span class="label">Notizen/Fragen:</span><i></i><i></i><i></i></div>
        </div>
      </div>
      <div class="service">
        <div class="service-photo" role="img" aria-label="Foto: helle Ladenpassage" style="background:linear-gradient(135deg,#e4edf2,#a9bfcc)"></div>
        <div class="need">Brauche ich: <b class="box"></b></div>
        <div class="service-body">
          <h3>Your Service One <span>Goes Here</span></h3>
          <p>Kurze Beschreibung der Leistung mit den wichtigsten Vorteilen für Händler vor Ort und online, klar und verständlich formuliert.</p>
          <div class="notes"><span class="label">Notizen/Fragen:</span><i></i><i></i><i></i></div>
        </div>
      </div>
    </div>
    <footer class="page-foot"><i class="band"></i><span class="title">Brochure Title Goes Here</span><span class="num">Seite 3</span></footer>
  </article>
</section>

<!-- Details + advantages -->
<section class="spread spread--advantages">
  <article class="page">
    <div class="brand page-brand"><b class="brand-dot"></b>sonnenhofmarktnord</div>
    <div class="service-list">
      <div class="service">
        <div class="service-photo" role="img" aria-label="Foto: Wohnhaus mit Garten" style="background:linear-gradient(135deg,#a9c4dc,#5d7d4a)"></div>
        <div class="need">Brauche ich: <b class="box"></b></div>
        <div class="service-body">
          <h3>Your Service One <span>Goes Here</span></h3>
          <p>Kurze Beschreibung der Leistung mit den wichtigsten Vorteilen für Händler vor Ort und online, klar und verständlich formuliert.</p>
          <div class="notes"><span class="label">Notizen/Fragen:</span><i></i><i></i><i></i></div>
        </div>
      </div>
      <div class="service">
        <div class="service-photo" role="img" aria-label="Foto: Altstadt am Wasser" style="background:linear-gradient(135deg,#3d78b8,#a4553a)"></div>
        <div class="need">Brauche ich: <b class="box"></b></div>
        <div class="service-body">
          <h3>Your Service One <span>Goes Here</span></h3>
          <p>Kurze Beschreibung der Leistung mit den wichtigsten Vorteilen für Händler vor Ort und online, klar und verständlich formuliert.</p>
          <div class="notes"><span class="label">Notizen/Fragen:</span><i></i><i></i><i></i></div>
        </div>
      </div>
      <div class="service">
        <div class="service-photo" role="img" aria-label="Foto: gedeckter Tisch mit Speisen" style="background:linear-gradient(135deg,#d99a3a,#4a6e8a)"></div>
        <div class="need">Brauche ich: <b class="box"></b></div>
        <div class="service-body">
          <h3>Your Service One <span>Goes Here</span></h3>
          <p>Kurze Beschreibung der Leistung mit den wichtigsten Vorteilen für Händler vor Ort und online, klar und verständlich formuliert.</p>
          <div class="notes"><span class="label">Notizen/Fragen:</span><i></i><i></i><i></i></div>
        </div>
      </div>
    </div>
    <footer class="page-foot"><i class="band"></i><span class="title">Brochure Title Goes Here</span><span class="num">Seite 4</span></footer>
  </article>

  <article class="page">
    <div class="brand page-brand"><b class="brand-dot"></b>sonnenhofmarktnord</div>
    <h2 class="adv-heading">... UND DAS WAR NOCH <span class="accent">LÄNGST NICHT ALLES</span>...</h2>
    <ul class="adv-list">
      <li><svg viewBox="0 0 16 16"><path d="M2 8.5 L6 12.5 L14 3" fill="none" stroke="#1f5fb8" stroke-width="2.6" stroke-linecap="round" stroke-linejoin="round"/></svg><p>Zusätzlicher Vorteil für Ihren Laden: mehr Sichtbarkeit in der Innenstadt und im Netz, persönliche Beratung und einfache Abläufe.</p></li>
      <li><svg viewBox="0 0 16 16"><path d="M2 8.5 L6 12.5 L14 3" fill="none" stroke="#1f5fb8" stroke-width="2.6" stroke-linecap="round" stroke-linejoin="round"/></svg><p>Zusätzlicher Vorteil für Ihren Laden: mehr Sichtbarkeit in der Innenstadt und im Netz, persönliche Beratung und einfache Abläufe.</p></li>
      <li><svg viewBox="0 0 16 16"><path d="M2 8.5 L6 12.5 L14 3" fill="none" stroke="#1f5fb8" stroke-width="2.6" stroke-linecap="round" stroke-linejoin="round"/></svg><p>Zusätzlicher Vorteil für Ihren Laden: mehr Sichtbarkeit in der Innenstadt und im Netz, persönliche Beratung und einfache Abläufe.</p></li>
      <li><svg viewBox="0 0 16 16"><path d="M2 8.5 L6 12.5 L14 3" fill="none" stroke="#1f5fb8" stroke-width="2.6" stroke-linecap="round" stroke-linejoin="round"/></svg><p>Zusätzlicher Vorteil für Ihren Laden: mehr Sichtbarkeit in der Innenstadt und im Netz, persönliche Beratung und einfache Abläufe.</p></li>
      <li><svg viewBox="0 0 16 16"><path d="M2 8.5 L6 12.5 L14 3" fill="none" stroke="#1f5fb8" stroke-width="2.6" stroke-linecap="round" stroke-linejoin="round"/></svg><p>Zusätzlicher Vorteil für Ihren Laden: mehr Sichtbarkeit in der Innenstadt und im Netz, persönliche Beratung und einfache Abläufe.</p></li>
      <li><svg viewBox="0 0 16 16"><path d="M2 8.5 L6 12.5 L14 3" fill="none" stroke="#1f5fb8" stroke-width="2.6" stroke-linecap="round" stroke-linejoin="round"/></svg><p>Zusätzlicher Vorteil für Ihren Laden: mehr Sichtbarkeit in der Innenstadt und im Netz, persönliche Beratung und einfache Abläufe.</p></li>
      <li><svg viewBox="0 0 16 16"><path d="M2 8.5 L6 12.5 L14 3" fill="none" stroke="#1f5fb8" stroke-width="2.6" stroke-linecap="round" stroke-linejoin="round"/></svg><p>Zusätzlicher Vorteil für Ihren Laden: mehr Sichtbarkeit in der Innenstadt und im Netz, persönliche Beratung und einfache Abläufe.</p></li>
      <li><svg viewBox="0 0 16 16"><path d="M2 8.5 L6 12.5 L14 3" fill="none" stroke="#1f5fb8" stroke-width="2.6" stroke-linecap="round" stroke-linejoin="round"/></svg><p>Zusätzlicher Vorteil für Ihren Laden: mehr Sichtbarkeit in der Innenstadt und im Netz, persönliche Beratung und einfache Abläufe.</p></li>
    </ul>
    <footer class="page-foot"><i class="band"></i><span class="title">Brochure Title Goes Here</span><span class="num">Seite 5</span></footer>
  </article>
</section>

</body>
</html>
```